Business Card Design Project

Looking for a square business card, 2"-2.5", with rounded corners. We specialize in exciting promotions with prize giveaways and our logo is attached.

I'm a fan of the sample card found here:
http://www.fernlowprints.com/25-X-25-Rounded-Corner-Business-Cards_p_204.html

Business card should show Name, Phone #, Email, Title and website.

Two design possibilities:
1. QR code on one side (we will determine what it is later, any QR code can be used for the design), with logo and info on the other side. It might be too hard to fit everything in this way.
2. Logo on one side, info on the other.

Flexible on our final choice, but looking to see some designs with a scannable QR code on one side and some without.

Sample details
Name: Marco Dustav
Phone: +1(416)555-0192
Email: marcodustav@pelbrooktally.com
Website: http://pelbrooktally.com

Target Market(s)

Internet startups

Industry/Entity Type

Business

Requirements
Must have
• Square design, most likely rounded corners
Nice to have
• QR code on one side, but seems like it would be hard to fit everything.

```html
<!DOCTYPE html>
<html lang="en">
<head>
<meta charset="utf-8">
<title>Marco Dustav – Square Business Card</title>
<link rel="stylesheet" href="https://fonts.googleapis.com/css2?family=Doto:wght@700&family=Pathway+Gothic+One&display=swap">
<style>
  :root {
    --stage: #000000;
    --navy: #214a8b;
    --cyan-light: #5ccbec;
    --cyan: #1ba3dc;
    --white: #ffffff;
    --ink: #1a1a1a;
    --brand-ink: #1c3f7c;
  }
  html, body {
    margin: 0;
    padding: 0;
    width: 1200px;
    height: 849px;
    overflow: hidden;
    background: var(--stage);
  }
  .stage {
    display: block;
    width: 1200px;
    height: 849px;
  }
  .card-name {
    font-family: "Doto", "Courier New", monospace;
    font-weight: 700;
    font-size: 27px;
    letter-spacing: 1px;
    fill: var(--white);
  }
  .contact-line {
    font-family: "Pathway Gothic One", "Arial Narrow", sans-serif;
    font-size: 16px;
    fill: var(--ink);
  }
  .brand-name {
    font-family: "Pathway Gothic One", "Arial Narrow", sans-serif;
    font-size: 50px;
    fill: var(--brand-ink);
  }
  .icon {
    fill: none;
    stroke: var(--white);
    stroke-width: 1.4;
    stroke-linecap: round;
    stroke-linejoin: round;
  }
</style>
</head>
<body>
<svg class="stage" viewBox="0 0 1171 828" xmlns="http://www.w3.org/2000/svg">
  <defs>
    <clipPath id="front-shape">
      <rect x="187" y="252" width="375" height="375" rx="34"/>
    </clipPath>
    <linearGradient id="sky" x1="0" y1="0" x2="0" y2="1">
      <stop offset="0" stop-color="var(--cyan-light)"/>
      <stop offset="1" stop-color="var(--cyan)"/>
    </linearGradient>
    <linearGradient id="glow" x1="0" y1="0" x2="1" y2="0">
      <stop offset="0" stop-color="var(--navy)" stop-opacity="0"/>
      <stop offset="1" stop-color="var(--cyan)" stop-opacity="0.9"/>
    </linearGradient>
  </defs>

  <g class="card-front" clip-path="url(#front-shape)">
    <rect x="187" y="252" width="375" height="375" fill="var(--navy)"/>
    <path d="M187,252 H562 V447 Q530,462 495,466 Q340,470 187,446 Z" fill="url(#sky)"/>
    <path d="M240,452 L320,627 L230,627 Z" fill="url(#glow)" opacity="0.7"/>
    <polygon points="222,252 495,252 495,627 320,627" fill="var(--white)"/>

    <text class="card-name" transform="translate(246,612) rotate(-90)">Marco Dustav</text>

    <text class="brand-name" x="385" y="345" text-anchor="middle">Pelbrook</text>
    <text class="brand-name" x="385" y="400" text-anchor="middle">Tally</text>

    <text class="contact-line" x="484" y="521" text-anchor="end">+1(416)555-0192</text>
    <text class="contact-line" x="484" y="547" text-anchor="end" textLength="142" lengthAdjust="spacingAndGlyphs">marcodustav@pelbrooktally.com</text>
    <text class="contact-line" x="484" y="573" text-anchor="end">http://pelbrooktally.com</text>

    <g class="icon icon-phone" transform="translate(506,505)">
      <path d="M3,2 L6,2 L7,6 L5,7.5 Q7,11 10.5,13 L12,11 L16,12 L16,15 Q9,16 5,11 Q2,7 3,2 Z"/>
    </g>
    <g class="icon icon-mail" transform="translate(505,533)">
      <rect x="1" y="1" width="16" height="12"/>
      <path d="M1,1 L9,8 L17,1 M1,13 L7,7 M17,13 L11,7"/>
    </g>
    <g class="icon icon-globe" transform="translate(505,558)">
      <circle cx="9" cy="9" r="7.5"/>
      <ellipse cx="9" cy="9" rx="3.2" ry="7.5"/>
      <path d="M1.5,9 H16.5 M3,5 H15 M3,13 H15"/>
    </g>
  </g>

  <rect class="card-back" x="585.5" y="222.5" width="375" height="375" rx="42"
        fill="var(--navy)" transform="rotate(-9 773 410)"/>
</svg>
</body>
</html>
```